Specialist aerospace company requires Powerpoint template

We are a company who delivers specialist engineering and testing services. We would like an updated Powerpoint template - specifically one that will be suitable to use in the production of training materials.
We would therefore like the following included:
-Our logo
-A copyright notice
-The course name (e.g. High Voltage Basics)
-The lesson name (e.g. Safe Clearances)
We wish to convey a professional image.

```html
<!DOCTYPE html>
<html lang="en">
<head>
<meta charset="utf-8">
<title>Altavolt Training Template</title>
<link rel="stylesheet" href="https://fonts.googleapis.com/css2?family=Exo+2:ital,wght@0,500;0,600;1,500;1,600;1,700&family=Poppins:wght@400;500&display=swap">
<style>
:root{
  --canvas:#8c8c8c;
  --blue:#4a77a5;
  --blue-deep:#3f6995;
  --slate:#4a5560;
  --mist:#d8dfe7;
  --ink:#111418;
  --body:#3a3f45;
  --white:#ffffff;
  --line:#4a77a5;
}
*{box-sizing:border-box;margin:0;padding:0}
html,body{width:1200px;height:4231px;overflow:hidden}
body{background:var(--canvas);position:relative;font-family:"Poppins",sans-serif;color:var(--body)}
.slide{position:absolute;left:60px;width:1080px;height:607px;background:var(--white);overflow:hidden}
.abs{position:absolute}
.photo{position:absolute}
.brand{position:absolute;display:flex;align-items:center;gap:8px;font-family:"Exo 2",sans-serif;font-weight:500;white-space:nowrap}
.brand .mark{display:block;background:currentColor}
.brand--small{color:var(--slate);font-size:22px}
.brand--small .mark{width:20px;height:20px}
.brand--white{color:var(--white)}
.heading{font-family:"Exo 2",sans-serif;font-style:italic;font-weight:600;color:var(--ink);position:absolute;white-space:nowrap}
.heading .accent{color:var(--blue)}
.kicker{font-family:"Exo 2",sans-serif;font-style:italic;font-weight:500;position:absolute;font-size:16px;color:var(--blue)}
.copy{position:absolute;font-size:10.5px;line-height:21px;text-align:justify;color:var(--body)}
.footer{position:absolute;left:0;right:0;bottom:22px;height:12px}
.footer .rule{position:absolute;top:6px;height:1.5px;background:var(--line)}
.footer .note{position:absolute;left:638px;top:0;font-size:9px;color:#555;white-space:nowrap}
.footer--light .rule{background:var(--white)}
.footer--light .note{color:var(--white)}
.agenda-item{position:absolute;left:523px;display:flex;align-items:center;gap:28px;font-family:"Exo 2",sans-serif;font-style:italic;font-weight:600;font-size:18px;color:var(--ink)}
.agenda-item .badge{width:58px;height:58px;border-radius:50%;background:var(--blue);display:flex;align-items:center;justify-content:center}
.contact{position:absolute;left:728px;display:flex;gap:14px;font-size:11px;color:#444;align-items:flex-start}
.contact svg{flex:none}
</style>
</head>
<body>

<!-- Title slide -->
<section class="slide" style="top:84px;background:var(--blue)">
  <div class="photo" role="img" aria-label="Faint background photo of a laptop keyboard on a desk" style="inset:0;background:linear-gradient(120deg,rgba(255,255,255,0.04),rgba(255,255,255,0.12) 70%,rgba(30,50,80,0.15))"></div>
  <div class="brand brand--white" style="left:72px;top:74px;font-size:44px"><span class="mark" style="width:38px;height:38px"></span>Altavolt</div>
  <div class="heading" style="left:80px;top:238px;font-size:32px;color:var(--white);font-weight:500">Welcome to</div>
  <div class="heading" style="left:80px;top:286px;font-size:62px;color:var(--white)">Altavolt</div>
  <svg class="abs" style="left:78px;top:417px" width="160" height="36" viewBox="0 0 160 36" aria-label="Social links">
    <g fill="none" stroke="#fff" stroke-width="1.5">
      <circle cx="17" cy="18" r="16"/><circle cx="56" cy="18" r="16"/><circle cx="95" cy="18" r="16"/><circle cx="134" cy="18" r="16"/>
    </g>
  </svg>
  <svg class="photo" style="left:560px;top:122px" width="420" height="360" viewBox="0 0 420 360" role="img" aria-label="Photo of engineers in hard hats reviewing a tablet in a factory">
    <defs><linearGradient id="g1" x1="0" y1="0" x2="1" y2="1"><stop offset="0" stop-color="#c9d2da"/><stop offset="0.5" stop-color="#8a949e"/><stop offset="1" stop-color="#4d5560"/></linearGradient></defs>
    <polygon points="44,8 412,8 380,354 4,354" fill="url(#g1)"/>
  </svg>
</section>

<!-- Agenda slide -->
<section class="slide" style="top:762px">
  <div class="abs" style="left:0;top:160px;width:46px;height:215px;background:var(--slate)"></div>
  <div class="abs" style="left:178px;top:440px;width:217px;height:75px;background:var(--blue)"></div>
  <div class="photo" role="img" aria-label="Photo of a hand ticking a checklist beside a laptop" style="left:46px;top:0;width:395px;height:467px;border-radius:0 0 24px 24px;background:linear-gradient(135deg,#6d8fad,#2f4d6c 55%,#b8c3cc)"></div>
  <div class="brand brand--small" style="left:880px;top:30px"><span class="mark"></span>Altavolt</div>
  <div class="heading" style="left:526px;top:66px;font-size:33px">Agenda</div>
  <div class="agenda-item" style="top:162px"><span class="badge"><svg width="28" height="28" viewBox="0 0 28 28" fill="none" stroke="#fff" stroke-width="1.6"><circle cx="14" cy="14" r="10"/><path d="M8 15l4-3 4 3 4-3"/></svg></span>About Us</div>
  <div class="agenda-item" style="top:247px"><span class="badge"><svg width="28" height="28" viewBox="0 0 28 28" fill="none" stroke="#fff" stroke-width="1.6"><path d="M14 4l11 20H3z"/><path d="M15 10l-3 6h4l-3 5"/></svg></span>High Voltage Basics</div>
  <div class="agenda-item" style="top:333px"><span class="badge"><svg width="28" height="28" viewBox="0 0 28 28" fill="none" stroke="#fff" stroke-width="1.6"><path d="M14 3l9 4v7c0 6-4 9-9 11-5-2-9-5-9-11V7z"/><path d="M10 14l3 3 5-6"/></svg></span>Safe Clearances</div>
  <div class="footer"><span class="rule" style="left:30px;width:588px"></span><span class="note">©Copyrights 2023 Altavolt &nbsp;|&nbsp; All Rights Reserved</span><span class="rule" style="left:907px;width:145px"></span></div>
</section>

<!-- About slide -->
<section class="slide" style="top:1448px">
  <div class="photo" role="img" aria-label="Photo of an engineer in a hard hat and safety glasses holding a laptop" style="left:0;top:0;width:510px;height:607px;border-radius:0 70px 70px 0;background:linear-gradient(160deg,#5a6470,#a3acb4 40%,#2c4f7d 75%,#3a3f45)"></div>
  <div class="brand brand--small" style="left:880px;top:30px"><span class="mark"></span>Altavolt</div>
  <div class="heading" style="left:597px;top:130px;font-size:34px">About <span class="accent">Us</span></div>
  <p class="copy" style="left:597px;top:208px;width:426px;line-height:22.5px">Lorem ipsum dolor sit amet, consectetur adipiscing elit, sed do eiusmod tempor incididunt ut labore et dolore magna aliqua. Ut enim ad minim veniam, quis nostrud exercitation ullamco laboris nisi ut aliquip ex ea commodo consequat. Duis aute irure dolor in reprehenderit in voluptate velit esse cillum dolore eu fugiat nulla pariatur. Excepteur sint occaecat cupidatat non proident, sunt in culpa qui officia deserunt mollit anim id est laborum. Sed ut perspiciatis unde omnis iste natus error sit voluptatem accusantium doloremque laudantium, totam rem aperiam, eaque ipsa quae ab illo inventore veritatis et quasi architecto beatae vitae dicta sunt explicabo. Nemo enim ipsam voluptatem quia voluptas sit aspernatur aut odit aut fugit, sed quia consequuntur magni dolores eos qui ratione voluptatem sequi nesciunt.</p>
  <div class="footer"><span class="rule" style="left:500px;width:118px"></span><span class="note">©Copyrights 2023 Altavolt &nbsp;|&nbsp; All Rights Reserved</span><span class="rule" style="left:907px;width:145px"></span></div>
</section>

<!-- Course slide -->
<section class="slide" style="top:2139px">
  <div class="abs" style="left:621px;top:0;width:459px;height:192px;background:var(--slate)"></div>
  <div class="brand brand--white" style="left:660px;top:62px;font-size:50px;gap:12px"><span class="mark" style="width:42px;height:42px"></span>Altavolt</div>
  <svg class="photo" style="left:69px;top:97px" width="470" height="434" viewBox="0 0 470 434" role="img" aria-label="Close-up photo of blue machined gears and shafts">
    <defs><linearGradient id="g2" x1="0" y1="0" x2="1" y2="1"><stop offset="0" stop-color="#3f6fc0"/><stop offset="0.5" stop-color="#1d3f8a"/><stop offset="1" stop-color="#c8ced4"/></linearGradient></defs>
    <polygon points="40,0 470,0 430,434 0,434" fill="url(#g2)"/>
  </svg>
  <div class="kicker" style="left:623px;top:233px">The course name</div>
  <div class="heading" style="left:623px;top:260px;font-size:34px">High Voltage <span class="accent">Basics</span></div>
  <p class="copy" style="left:623px;top:334px;width:400px;line-height:24.6px">Lorem ipsum dolor sit amet, consectetur adipiscing elit, sed do eiusmod tempor incididunt ut labore et dolore magna aliqua. Ut enim ad minim veniam, quis nostrud exercitation ullamco laboris nisi ut aliquip ex ea commodo consequat. Duis aute irure dolor in reprehenderit in voluptate velit esse cillum dolore eu fugiat nulla pariatur. Excepteur sint occaecat cupidatat non proident, sunt in culpa qui officia deserunt mollit anim id est laborum.</p>
  <div class="footer"><span class="rule" style="left:30px;width:588px"></span><span class="note">©Copyrights 2023 Altavolt &nbsp;|&nbsp; All Rights Reserved</span><span class="rule" style="left:907px;width:145px"></span></div>
</section>

<!-- Lesson slide -->
<section class="slide" style="top:2842px;background:var(--blue)">
  <svg class="photo" style="left:0;top:0" width="1080" height="607" viewBox="0 0 1080 607" role="img" aria-label="Photo of two engineers in hard hats on a construction site with cranes">
    <defs><linearGradient id="g3" x1="0" y1="0" x2="0" y2="1"><stop offset="0" stop-color="#9fb4c9"/><stop offset="0.45" stop-color="#c7a98a"/><stop offset="1" stop-color="#2e3640"/></linearGradient></defs>
    <polygon points="462,0 1080,0 1080,607 621,607" fill="url(#g3)"/>
  </svg>
  <div class="brand brand--white" style="left:880px;top:30px;font-size:22px"><span class="mark" style="width:20px;height:20px"></span>Altavolt</div>
  <div class="kicker" style="left:53px;top:182px;color:var(--white)">The lesson name</div>
  <div class="heading" style="left:53px;top:208px;font-size:34px;color:var(--white);font-weight:500">Safe Clearances</div>
  <p class="copy" style="left:53px;top:284px;width:400px;line-height:24.6px;color:#e6edf4">Lorem ipsum dolor sit amet, consectetur adipiscing elit, sed do eiusmod tempor incididunt ut labore et dolore magna aliqua. Ut enim ad minim veniam, quis nostrud exercitation ullamco laboris nisi ut aliquip ex ea commodo consequat. Duis aute irure dolor in reprehenderit in voluptate velit esse cillum dolore eu fugiat nulla pariatur. Excepteur sint occaecat cupidatat non proident, sunt in culpa qui officia deserunt mollit anim id est laborum.</p>
  <div class="footer footer--light"><span class="rule" style="left:30px;width:588px"></span><span class="note">©Copyrights 2023 Altavolt &nbsp;|&nbsp; All Rights Reserved</span><span class="rule" style="left:907px;width:145px"></span></div>
</section>

<!-- Closing slide -->
<section class="slide" style="top:3538px">
  <div class="photo" role="img" aria-label="Photo of an engineer in a hard hat with a laptop beside orange industrial robots" style="left:0;top:0;width:663px;height:607px;background:linear-gradient(135deg,#c8cdd2,#d9792e 45%,#3f6e84 70%,#2a2f35)"></div>
  <div class="abs" style="left:663px;top:0;width:417px;height:271px;background:var(--mist)"></div>
  <div class="brand" style="left:692px;top:106px;font-size:50px;gap:12px;color:var(--slate)"><span class="mark" style="width:42px;height:42px"></span>Altavolt</div>
  <div class="abs" style="left:722px;top:318px;font-family:'Exo 2',sans-serif;font-weight:600;font-size:38px;color:var(--blue);letter-spacing:1px">THANK YOU</div>
  <div class="contact" style="top:396px"><svg width="14" height="14" viewBox="0 0 14 14" fill="var(--slate)"><path d="M3 1l2.5 2.5-1.4 1.8c.8 1.8 2.1 3.1 3.9 3.9l1.8-1.4L12.3 10.3 11 13C6 13 1 8 1 3z"/></svg>+1 (555) 010 0199</div>
  <div class="contact" style="top:434px"><svg width="14" height="14" viewBox="0 0 14 14" fill="none" stroke="var(--slate)" stroke-width="1.4"><circle cx="7" cy="7" r="6"/><path d="M1 7h12M7 1c2.5 3 2.5 9 0 12M7 1c-2.5 3-2.5 9 0 12"/></svg>www.altavolt.example</div>
  <div class="contact" style="top:472px"><svg width="14" height="14" viewBox="0 0 14 14" fill="var(--slate)"><path d="M1 3h12v8H1z"/><path d="M1 3l6 5 6-5" stroke="#fff" stroke-width="1" fill="none"/></svg>info@altavolt.example</div>
  <div class="contact" style="top:503px"><svg width="14" height="16" viewBox="0 0 14 16" fill="var(--slate)"><path d="M7 0a5.5 5.5 0 0 0-5.5 5.5C1.5 10 7 16 7 16s5.5-6 5.5-10.5A5.5 5.5 0 0 0 7 0zm0 7.5a2 2 0 1 1 0-4 2 2 0 0 1 0 4z"/></svg><span>123,Lorem ipsum dolor<br>sit amet.</span></div>
</section>

</body>
</html>
```